Calloway Ridge Associates Stationery

Use attached logo for stationery
Stationery, Letterhead and Envelope + Business cards

Tag line: Walking alongside those doing the work of the Gospel

```html
<!DOCTYPE html>
<html lang="en">
<head>
<meta charset="utf-8">
<title>Calloway Ridge Associates Stationery</title>
<link href="https://fonts.googleapis.com/css2?family=Cinzel:wght@500&family=Montserrat:wght@400;600&display=swap" rel="stylesheet">
<style>
  :root {
    --backdrop: #cfcfcf;
    --paper: #ffffff;
    --navy: #1d5a8e;
    --navy-deep: #174d7c;
    --sky: #5fd0e6;
    --ink: #1f5b91;
    --muted: #4a5866;
  }
  * { box-sizing: border-box; margin: 0; padding: 0; }
  html, body { width: 1200px; height: 1056px; overflow: hidden; }
  body { background: var(--backdrop); font-family: "Montserrat", sans-serif; position: relative; }

  .piece { position: absolute; background: var(--paper); overflow: hidden; }
  .wordmark {
    font-family: "Cinzel", serif; font-weight: 500; color: var(--ink);
    text-align: center; line-height: 1.1; letter-spacing: .04em;
  }
  .wordmark.on-navy { color: var(--paper); }
  .wordmark .sub { display: block; letter-spacing: .35em; font-size: .55em; }
  .wave { position: absolute; left: 0; bottom: 0; width: 100%; }
  .web { position: absolute; right: 8px; bottom: 4px; color: var(--paper); font-size: 4px; font-weight: 600; }
  .contact { position: absolute; font-size: 3.6px; color: var(--muted); line-height: 1.45; }
  .contact strong { color: var(--ink); font-weight: 600; display: block; }

  /* letterhead */
  .letterhead { left: 94px; top: 62px; width: 306px; height: 432px; }
  .letterhead .wordmark { position: absolute; left: 26px; top: 52px; font-size: 10px; }
  .letterhead .contact { left: 214px; top: 32px; }
  .letterhead .wave { height: 30px; }

  /* open envelope */
  .envelope-open { left: 446px; top: 122px; width: 320px; height: 218px; background: transparent; }
  .envelope-open .body { position: absolute; left: 0; top: 58px; width: 100%; height: 160px; background: var(--paper); }
  .envelope-open .liner { position: absolute; left: 22px; top: 0; width: 276px; height: 93px; background: var(--navy); border-radius: 6px 6px 0 0; }
  .envelope-open .flap { position: absolute; left: 0; top: 0; width: 100%; height: 60px; background: var(--navy-deep); clip-path: polygon(2% 0, 98% 0, 100% 100%, 0 100%); border-radius: 8px 8px 0 0; }

  /* envelope front */
  .envelope-front { left: 803px; top: 122px; width: 321px; height: 160px; }
  .envelope-front .wordmark { position: absolute; left: 16px; top: 46px; font-size: 10px; }
  .envelope-front .contact { left: 35px; top: 134px; }
  .envelope-front .wave { height: 28px; }

  /* envelope back */
  .envelope-back { left: 805px; top: 328px; width: 321px; height: 161px; }
  .envelope-back .flap { position: absolute; left: 0; top: 0; width: 100%; height: 62px; background: var(--navy); border-radius: 0 0 8px 8px; display: flex; align-items: center; justify-content: center; }
  .envelope-back .wordmark { font-size: 6px; }

  /* business cards */
  .card { top: 411px; width: 124px; height: 80px; }
  .card-front { left: 453px; }
  .card-front .wordmark { position: absolute; left: 8px; top: 38px; font-size: 6.5px; }
  .card-front .contact { left: 71px; top: 24px; font-size: 2.8px; }
  .card-front .wave { height: 10px; }
  .card-back { left: 626px; background: var(--navy); display: flex; align-items: center; justify-content: center; }
  .card-back .wordmark { font-size: 7px; }

  /* folder front */
  .folder-front { left: 70px; top: 538px; width: 332px; height: 446px; background: var(--navy); }
  .folder-front .wordmark { position: absolute; left: 0; right: 0; top: 56px; font-size: 21px; }

  /* open folder */
  .folder-open { left: 452px; top: 534px; width: 666px; height: 447px; background: #f1f1f1; }
  .folder-open .insert { position: absolute; left: 351px; top: 6px; width: 306px; height: 296px; background: var(--paper); }
  .folder-open .insert .wordmark { position: absolute; left: 30px; top: 54px; font-size: 10px; }
  .folder-open .insert .contact { left: 214px; top: 36px; }
  .pocket { position: absolute; top: 300px; height: 147px; background: var(--navy); }
  .pocket-left { left: 0; width: 329px; clip-path: polygon(0 0, 96% 0, 100% 100%, 0 100%); border-radius: 0 10px 0 0; }
  .pocket-right { left: 340px; width: 326px; clip-path: polygon(4% 0, 100% 0, 100% 100%, 0 100%); border-radius: 10px 0 0 0; }
  .pocket-right .wordmark { position: absolute; right: 26px; bottom: 18px; font-size: 10px; }
</style>
</head>
<body>

<svg width="0" height="0" style="position:absolute">
  <defs>
    <symbol id="footer-wave" viewBox="0 0 300 30" preserveAspectRatio="none">
      <path d="M0 30 L0 16 Q40 26 130 20 Q220 12 300 6 L300 30 Z" fill="#1d5a8e"/>
      <path d="M100 22 Q200 10 300 4 L300 9 Q210 14 100 22 Z" fill="#5fd0e6"/>
    </symbol>
  </defs>
</svg>

<section class="piece letterhead">
  <div class="wordmark">CALLOWAY RIDGE<span class="sub">ASSOCIATES</span></div>
  <div class="contact">
    <strong>CALLOWAY RIDGE ASSOCIATES</strong>
    48 Juniper Hollow Way<br>Fairmont, NC 28340<br>
    &#9990; 555-014-2290<br>&#9993; info@callowayridge.org
  </div>
  <svg class="wave"><use href="#footer-wave"/></svg>
  <span class="web">www.callowayridge.org</span>
</section>

<section class="piece envelope-open">
  <div class="body"></div>
  <div class="liner"></div>
  <div class="flap"></div>
</section>

<section class="piece envelope-front">
  <div class="wordmark">CALLOWAY RIDGE<span class="sub">ASSOCIATES</span></div>
  <div class="contact">48 Juniper Hollow Way<br>Fairmont, NC 28340</div>
  <svg class="wave"><use href="#footer-wave"/></svg>
  <span class="web">www.callowayridge.org</span>
</section>

<section class="piece envelope-back">
  <div class="flap"><div class="wordmark on-navy">CALLOWAY RIDGE<span class="sub">ASSOCIATES</span></div></div>
</section>

<section class="piece card card-front">
  <div class="wordmark">CALLOWAY RIDGE<span class="sub">ASSOCIATES</span></div>
  <div class="contact">
    <strong>JORDAN ELLERY</strong>Director<br>
    &#9990; 555-014-2290<br>&#9993; info@callowayridge.org<br>www.callowayridge.org<br>
    48 Juniper Hollow Way<br>Fairmont, NC 28340
  </div>
  <svg class="wave"><use href="#footer-wave"/></svg>
</section>

<section class="piece card card-back">
  <div class="wordmark on-navy">CALLOWAY RIDGE<span class="sub">ASSOCIATES</span></div>
</section>

<section class="piece folder-front">
  <div class="wordmark on-navy">CALLOWAY RIDGE<span class="sub">ASSOCIATES</span></div>
</section>

<section class="piece folder-open">
  <div class="insert">
    <div class="wordmark">CALLOWAY RIDGE<span class="sub">ASSOCIATES</span></div>
    <div class="contact">
      <strong>CALLOWAY RIDGE ASSOCIATES</strong>
      48 Juniper Hollow Way<br>Fairmont, NC 28340<br>
      &#9990; 555-014-2290<br>&#9993; info@callowayridge.org
    </div>
  </div>
  <div class="pocket pocket-left"></div>
  <div class="pocket pocket-right">
    <div class="wordmark on-navy">CALLOWAY RIDGE<span class="sub">ASSOCIATES</span></div>
  </div>
</section>

</body>
</html>
```